Brightwire Hollow Business cards

one side I would like my logo (uploaded) and the other side I want my details. I'm an electrician in sydney. The logo side I'm happy with just a white background and our logo in the middle.

Details for other side
24/7 Sydney Electrician
Marcus Pell
0431 587 219
marcus@brightwirehollow.com.au
brightwirehollow.com.au
icons for facebook, instagram, linked in

Industry/Entity Type

electrician

Contact Information for Business Card

company info

```html
<!DOCTYPE html>
<html lang="en">
<head>
<meta charset="utf-8">
<title>Brightwire Hollow – Business Cards</title>
<link rel="stylesheet" href="https://fonts.googleapis.com/css2?family=Rubik:wght@400;500;700&display=swap">
<style>
  :root {
    --stage: #d4d4d4;
    --card: #ffffff;
    --red: #ec3323;
    --ink: #1d1d1d;
    --blush: #fdece4;
    --shadow: rgba(0,0,0,0.28);
  }
  * { box-sizing: border-box; margin: 0; padding: 0; }
  html, body {
    width: 1200px; height: 780px; overflow: hidden;
    background: var(--stage);
    font-family: "Rubik", sans-serif;
  }
  .stage {
    width: 1200px; height: 780px;
    display: flex; align-items: center; justify-content: center; gap: 32px;
  }
  .card {
    position: relative;
    width: 560px; height: 342px;
    background: var(--card);
    box-shadow: 0 14px 30px var(--shadow);
    overflow: hidden;
  }

  /* details side */
  .card-details .brand {
    position: absolute; left: 30px; top: 28px;
    color: var(--red); font-weight: 700; font-size: 34px;
    line-height: 1; letter-spacing: 0.5px; text-transform: uppercase;
  }
  .card-details .rule {
    position: absolute; left: 30px; top: 112px;
    width: 470px; height: 1.5px; background: var(--red);
  }
  .contact-list {
    position: absolute; left: 30px; top: 138px;
    list-style: none; color: var(--ink);
    font-size: 13.5px; font-weight: 500;
  }
  .contact-list li { display: flex; align-items: center; gap: 8px; margin-bottom: 6px; }
  .contact-list li.phone { font-size: 16px; }
  .contact-list svg { width: 14px; height: 14px; flex: none; }
  .decor-circle {
    position: absolute; left: 370px; top: 140px;
    width: 170px; height: 170px; border-radius: 50%;
    background: var(--blush);
  }
  .person {
    position: absolute; right: 30px; top: 172px; text-align: right;
  }
  .person .name { color: var(--red); font-weight: 700; font-size: 30px; line-height: 1; }
  .person .role { color: var(--ink); font-weight: 500; font-size: 13px; margin-top: 4px; }
  .person .underline { height: 1.5px; background: var(--red); width: 190px; margin: 8px 0 0 auto; }
  .tagline {
    position: absolute; right: 30px; top: 262px;
    color: var(--red); font-weight: 500; font-size: 15px;
    letter-spacing: 0.5px; text-transform: uppercase;
  }
  .wave { position: absolute; left: 0; bottom: 0; width: 560px; height: 342px; }
  .social {
    position: absolute; left: 232px; bottom: 14px;
    display: flex; gap: 10px;
  }
  .social span { width: 16px; height: 16px; border-radius: 50%; background: var(--card); }

  /* logo side */
  .card-logo { display: flex; align-items: center; justify-content: center; }
  .card-logo .brand {
    color: var(--red); font-weight: 700; font-size: 56px;
    line-height: 1.05; text-align: center; text-transform: uppercase; letter-spacing: 1px;
  }
</style>
</head>
<body>
<main class="stage">

  <section class="card card-details" aria-label="Business card, details side">
    <div class="decor-circle"></div>
    <svg class="wave" viewBox="0 0 560 342" aria-hidden="true">
      <path d="M0 218 C150 250 300 280 470 342 L0 342 Z" fill="var(--red)"/>
      <path d="M0 250 C200 262 390 290 560 342 L0 342 Z" fill="var(--ink)"/>
      <path d="M120 260 C250 268 360 292 480 342 L560 342 C420 300 260 266 120 260 Z" fill="var(--ink)"/>
    </svg>
    <div class="brand">Brightwire Hollow</div>
    <div class="rule"></div>
    <ul class="contact-list">
      <li class="phone">
        <svg viewBox="0 0 24 24"><path fill="var(--red)" d="M6.6 10.8a15 15 0 0 0 6.6 6.6l2.2-2.2c.3-.3.7-.4 1-.2 1.1.4 2.3.6 3.6.6.6 0 1 .4 1 1V20c0 .6-.4 1-1 1A17 17 0 0 1 3 4c0-.6.4-1 1-1h3.5c.6 0 1 .4 1 1 0 1.3.2 2.5.6 3.6.1.3 0 .7-.2 1z"/></svg>
        0431 587 219
      </li>
      <li>
        <svg viewBox="0 0 24 24"><circle cx="12" cy="12" r="10" fill="var(--red)"/><path d="M2 12h20M12 2c3 3 3 17 0 20M12 2c-3 3-3 17 0 20" stroke="#fff" stroke-width="1.4" fill="none"/></svg>
        www.brightwirehollow.com.au
      </li>
      <li>
        <svg viewBox="0 0 24 24"><rect x="2" y="5" width="20" height="14" rx="1.5" fill="var(--red)"/><path d="M2.5 6l9.5 7 9.5-7" stroke="#fff" stroke-width="1.5" fill="none"/></svg>
        marcus@brightwirehollow.com.au
      </li>
    </ul>
    <div class="person">
      <div class="name">Marcus Pell</div>
      <div class="role">Electrician</div>
      <div class="underline"></div>
    </div>
    <div class="tagline">24/7 Sydney Electrician</div>
    <div class="social" aria-label="Social media links"><span></span><span></span><span></span></div>
  </section>

  <section class="card card-logo" aria-label="Business card, logo side">
    <div class="brand">Brightwire<br>Hollow</div>
  </section>

</main>
</body>
</html>
```